Post it Note design

POST-IT NOTE DESIGN (CONTENT)
Size recommended: 4x6 for handwriting space.
Header (Bold):
Lighting Issue Detected on Your Property
Sub-header:
During our routine night inspection, we noted the following item(s):
Checkbox List:
⬜ Building Lights Out
⬜ Pole Lights Out
⬜ Sign Not Illuminated
⬜ Other ________________________
Action Line:
We can provide a quote or dispatch service right away.
Area for notes
Contact Block (Bold & Centered):
Brovane Fixture Inc.
Service@BrovaneFixture.com
www.BrovaneFixture.com
877-514-0862
Industry/Entity Type
Electrical lighting
Colors
Designer to choose colors to be used in the design.
Look and feel
Each slider illustrates characteristics of the customer's brand and the style your logo design should communicate.

```html
<!DOCTYPE html>
<html lang="en">
<head>
<meta charset="utf-8">
<title>Brovane Fixture – Lighting Issue Postcard</title>
<link rel="stylesheet" href="https://fonts.googleapis.com/css2?family=Poppins:wght@400;500;600&family=Roboto+Slab:wght@700;800&display=swap">
<style>
  :root {
    --stage: #a1acf6;
    --navy: #1b2256;
    --navy-deep: #151c4a;
    --red: #e91e25;
    --paper: #f3f3f3;
    --paper-grey: #e4e4e6;
    --ink: #15151a;
    --rule: #c9c9cc;
    --white: #ffffff;
  }
  * { margin: 0; padding: 0; box-sizing: border-box; }
  html, body { width: 891px; height: 1200px; overflow: hidden; }
  body {
    background: var(--stage);
    font-family: "Poppins", sans-serif;
    position: relative;
  }
  .card {
    position: absolute;
    left: 88px;
    width: 712px;
    height: 474px;
    overflow: hidden;
    box-shadow: 0 4px 14px rgba(30, 40, 120, 0.18);
  }
  .card--front { top: 94px; background: var(--navy); }
  .card--back { top: 624px; background: linear-gradient(90deg, #dcdcde, #f0f0f1); }
  .card__shapes { position: absolute; inset: 0; width: 100%; height: 100%; }
  .abs { position: absolute; }

  .photo {
    position: absolute;
    border-radius: 2px;
  }
  .photo--technician {
    left: 0; top: 0; width: 354px; height: 240px;
    background: linear-gradient(160deg, #3f6fb0 0%, #6f9ad0 45%, #b7c2cc 75%, #8c9296 100%);
  }
  .photo--truck {
    left: 510px; top: 253px; width: 183px; height: 114px;
    background: linear-gradient(180deg, #d9dde3 0%, #f4f5f6 50%, #9ea3a8 100%);
    border-radius: 10px;
  }
  .photo--van {
    left: 46px; top: 287px; width: 243px; height: 170px;
    background: linear-gradient(160deg, #f2f3f4 0%, #d6d9dd 60%, #7d8187 100%);
    border-radius: 14px;
  }

  .brand-name {
    font-family: "Poppins", sans-serif;
    font-weight: 600;
    color: var(--red);
    line-height: 1.05;
    letter-spacing: 0.5px;
  }
  .brand-name--front { left: 520px; top: 24px; width: 180px; font-size: 26px; text-align: center; }
  .brand-name--back { left: 36px; top: 56px; font-size: 26px; }

  .headline {
    left: 367px; top: 140px;
    font-family: "Roboto Slab", serif;
    font-weight: 800;
    font-size: 30px;
    line-height: 35px;
    color: var(--white);
    text-transform: uppercase;
  }
  .headline__accent { color: var(--red); }

  .inspection-intro {
    left: 28px; top: 272px;
    font-family: "Roboto Slab", serif;
    font-weight: 700;
    font-size: 12.3px;
    line-height: 18px;
    color: var(--ink);
    text-transform: uppercase;
  }
  .checklist { left: 28px; top: 316px; list-style: none; }
  .checklist__item {
    display: flex; align-items: center;
    height: 24px;
    font-size: 11px; font-weight: 500; color: var(--ink);
  }
  .checklist__box {
    width: 8px; height: 8px;
    border: 1.3px solid var(--red);
    margin-right: 7px;
  }
  .checklist__blank {
    display: inline-block;
    width: 151px; height: 1px;
    background: var(--rule);
    margin-left: 17px; margin-top: 6px;
  }
  .action-line {
    left: 305px; top: 316px;
    font-size: 8.6px; line-height: 13px; font-weight: 500; color: var(--ink);
  }
  .note-rule { left: 305px; width: 195px; height: 1px; background: var(--rule); }

  .contact-bar {
    left: 108px; top: 444px; width: 456px; height: 32px;
    background: var(--red);
    border-radius: 16px 16px 0 0;
    display: flex; align-items: center; justify-content: space-evenly;
    color: var(--white); font-size: 8.8px;
    padding-bottom: 2px;
  }
  .contact-bar__item { display: flex; align-items: center; gap: 4px; }
  .icon { display: block; fill: currentColor; flex-shrink: 0; }

  .contact-block { left: 33px; top: 140px; color: var(--white); }
  .contact-block__company { font-size: 17.5px; font-weight: 500; margin-bottom: 8px; }
  .contact-block__line {
    display: flex; align-items: center; gap: 8px;
    font-size: 18px; font-weight: 500; height: 33px;
  }
  .stamp-box { left: 597px; top: 17px; width: 104px; height: 94px; background: var(--paper); }
  .address-rule { left: 416px; width: 275px; height: 1px; background: #cfcfd2; }
</style>
</head>
<body>

<!-- Front of the card -->
<section class="card card--front" aria-label="Postcard front">
  <div class="photo photo--technician" role="img" aria-label="Photo of a technician in a bucket lift servicing pole-mounted floodlights against a blue sky"></div>

  <svg class="card__shapes" viewBox="0 0 712 474" preserveAspectRatio="none" aria-hidden="true">
    <!-- top-right brand panel -->
    <path d="M428 0 C470 80 560 130 712 138 V0 Z" fill="var(--red)"/>
    <path d="M444 0 C486 72 570 118 712 126 V0 Z" fill="#f5f5f5"/>
    <!-- lower content panel -->
    <path d="M0 228 C170 210 360 230 520 310 C600 352 665 410 700 474 H0 Z" fill="var(--red)"/>
    <path d="M0 258 C170 232 350 250 505 323 C590 362 650 420 685 474 H0 Z" fill="#f4f4f4"/>
  </svg>

  <p class="abs brand-name brand-name--front">Brovane Fixture</p>

  <h1 class="abs headline">
    <span class="headline__accent">Lighting Issue</span><br>
    <span class="headline__accent">Detected</span> on your<br>
    property
  </h1>

  <div class="photo photo--truck" role="img" aria-label="Photo of a white bucket truck with orange safety cones"></div>

  <p class="abs inspection-intro">During our routine night inspection,<br>we noted the following item(s)</p>

  <ul class="abs checklist">
    <li class="checklist__item"><span class="checklist__box"></span>Building Lights Out</li>
    <li class="checklist__item"><span class="checklist__box"></span>Pole Lights Out</li>
    <li class="checklist__item"><span class="checklist__box"></span>Sign Not Illuminated</li>
    <li class="checklist__item"><span class="checklist__box"></span>Other<span class="checklist__blank"></span></li>
  </ul>

  <p class="abs action-line">We can provide a quote or dispatch<br>service right away.</p>
  <div class="abs note-rule" style="top:360px"></div>
  <div class="abs note-rule" style="top:380px"></div>
  <div class="abs note-rule" style="top:399px"></div>

  <div class="abs contact-bar">
    <span class="contact-bar__item">
      <svg class="icon" width="9" height="7" viewBox="0 0 16 12"><path d="M0 0h16v2L8 7 0 2z"/><path d="M0 4l8 5 8-5v8H0z"/></svg>
      Service@BrovaneFixture.com
    </span>
    <span class="contact-bar__item">
      <svg class="icon" width="8" height="8" viewBox="0 0 16 16"><circle cx="8" cy="8" r="8"/><path d="M4 4c2 0 3 2 2 3s1 3 0 5M11 2c-1 2 1 3 3 3" stroke="var(--red)" stroke-width="1.6" fill="none"/></svg>
      www.BrovaneFixture.com
    </span>
    <span class="contact-bar__item">
      <svg class="icon" width="8" height="8" viewBox="0 0 16 16"><path d="M3 0l3 4-2 2c1 3 3 5 6 6l2-2 4 3-2 3C7 16 0 9 0 3z"/></svg>
      877-514-0862
    </span>
  </div>
</section>

<!-- Back of the card -->
<section class="card card--back" aria-label="Postcard back">
  <svg class="card__shapes" viewBox="0 0 712 474" preserveAspectRatio="none" aria-hidden="true">
    <path d="M0 0 H252 C340 50 392 150 390 250 C388 340 350 420 284 474 H0 Z" fill="var(--red)"/>
    <path d="M0 0 H246 C334 52 386 150 384 250 C382 340 344 420 278 474 H0 Z" fill="#f4f4f4"/>
    <path d="M0 0 H244 C330 54 380 150 380 250 C378 340 340 420 274 474 H0 Z" fill="var(--navy-deep)"/>
  </svg>

  <p class="abs brand-name brand-name--back">Brovane<br>Fixture</p>

  <div class="abs contact-block">
    <p class="contact-block__company">Brovane Fixture Inc.</p>
    <p class="contact-block__line">
      <svg class="icon" width="17" height="13" viewBox="0 0 16 12"><path d="M0 0h16v2L8 7 0 2z"/><path d="M0 4l8 5 8-5v8H0z"/></svg>
      Service@BrovaneFixture.com
    </p>
    <p class="contact-block__line">
      <svg class="icon" width="15" height="15" viewBox="0 0 16 16"><circle cx="8" cy="8" r="8"/><path d="M4 4c2 0 3 2 2 3s1 3 0 5M11 2c-1 2 1 3 3 3" stroke="var(--navy-deep)" stroke-width="1.6" fill="none"/></svg>
      www.BrovaneFixture.com
    </p>
    <p class="contact-block__line">
      <svg class="icon" width="14" height="14" viewBox="0 0 16 16"><path d="M3 0l3 4-2 2c1 3 3 5 6 6l2-2 4 3-2 3C7 16 0 9 0 3z"/></svg>
      877-514-0862
    </p>
  </div>

  <div class="photo photo--van" role="img" aria-label="Photo of a white company service van with roof ladder rack"></div>

  <div class="abs stamp-box" aria-label="Stamp area"></div>
  <div class="abs address-rule" style="top:172px"></div>
  <div class="abs address-rule" style="top:231px"></div>
  <div class="abs address-rule" style="top:288px"></div>
  <div class="abs address-rule" style="top:347px"></div>
</section>

</body>
</html>
```